Business card design for global fintech startup

Veltrix is a modern payments platform for the global insurance industry, serving international health, life, and travel insurers, MGAs, brokers, and partners.

We need a professional, premium business card for use at insurance conferences and executive meetings. The goal is to create a card that feels trustworthy, modern, and high-quality, while still being distinctive and memorable in a stack of business cards.

Target audience:
Senior insurance executives (VP, C-suite).

Design goals:
Clear, professional, and credible
Modern but not trendy
Premium and well-structured
Easy to read and practical for networking

Brand direction:
Brand-first (company over individual)
Follow existing brand guidelines where possible
Clean layout, strong hierarchy, excellent readability

Must include:
Name
Title
Company name (Veltrix)
Logo
Email
Phone/Whatsapp
Website (www.withveltrix.example)
Tagline - Speed that earns trust

Materials & finish:
Open to designer recommendations for premium look and feel.

Please avoid:
Flashy or trendy startup styles
Generic insurance icons or clichés
Cluttered layouts or hard-to-read text

Deliverables:
Front and back business card, print-ready files.

Target Market(s)

Global Insurance executives

Industry/Entity Type

Fintech, Insurtech, Insurance, Financial Services

Contact Information for Business Card

Name Title Company name (Veltrix) Logo Email Phone/Whatsapp Website (www.withveltrix.example) Tagline - Speed that earns trust

Font styles to use
Other font styles liked:
• See brand guidelines

Requirements
Nice to have
• something that stands out/makes us more memorable while still remaining professional
Should not have
• Please avoid: Flashy or trendy startup styles Generic insurance icons or clichés Cluttered layouts or hard-to-read text

```html
<!DOCTYPE html>
<html lang="en">
<head>
<meta charset="utf-8">
<title>Veltrix — Business Card, Front and Back</title>
<link rel="stylesheet" href="https://fonts.googleapis.com/css2?family=Montserrat:wght@500;600;700&family=Open+Sans:wght@400&display=swap">
<style>
  :root {
    --page-bg: #e6e8ea;
    --card-white: #f4f4f3;
    --ink: #111111;
    --brand-purple: #5a2f92;
    --brand-blue: #2f7db9;
    --tint-lavender: #dcd6ea;
    --tint-teal: #cfe6ea;
    --card-shadow: rgba(0, 0, 0, 0.18);
  }
  * { box-sizing: border-box; margin: 0; padding: 0; }
  html, body {
    width: 1200px;
    height: 900px;
    overflow: hidden;
    background: var(--page-bg);
  }
  .canvas {
    position: relative;
    width: 1200px;
    height: 900px;
  }
  .card {
    position: absolute;
    left: 320px;
    width: 560px;
    height: 320px;
    border-radius: 4px;
    box-shadow: 0 10px 28px var(--card-shadow);
    overflow: hidden;
  }
  /* Front */
  .card-front {
    top: 100px;
    background:
      radial-gradient(circle at 0% 0%, var(--tint-lavender) 0%, transparent 55%),
      radial-gradient(circle at 0% 100%, var(--tint-teal) 0%, transparent 55%),
      var(--card-white);
  }
  .front-lockup {
    position: absolute;
    left: 0;
    right: 0;
    top: 0;
    bottom: 0;
    display: flex;
    align-items: center;
    justify-content: center;
    gap: 28px;
  }
  .brand-name-front {
    display: flex;
    align-items: center;
    gap: 9px;
    font-family: "Montserrat", sans-serif;
    font-weight: 600;
    font-size: 16px;
    letter-spacing: 0.14em;
    color: var(--ink);
  }
  .brand-dot {
    width: 14px;
    height: 14px;
    border-radius: 50%;
    background: var(--brand-purple);
    flex: none;
  }
  .tagline {
    font-family: "Montserrat", sans-serif;
    font-weight: 700;
    font-size: 38px;
    line-height: 1.05;
    color: var(--ink);
  }
  .tagline-accent { display: block; color: var(--brand-purple); }

  /* Back */
  .card-back {
    top: 480px;
    background: var(--card-white);
  }
  .person {
    position: absolute;
    left: 60px;
    top: 64px;
  }
  .person-name {
    font-family: "Montserrat", sans-serif;
    font-weight: 700;
    font-size: 22px;
    letter-spacing: 0.02em;
    color: var(--brand-blue);
    text-transform: uppercase;
  }
  .person-title {
    font-family: "Open Sans", sans-serif;
    font-size: 15px;
    color: var(--ink);
    margin-top: 2px;
  }
  .contact {
    position: absolute;
    left: 60px;
    bottom: 46px;
    list-style: none;
    font-family: "Open Sans", sans-serif;
    font-size: 16px;
    line-height: 1.35;
    color: var(--ink);
  }
  .wordmark {
    position: absolute;
    right: 48px;
    bottom: 92px;
    display: flex;
    align-items: center;
    gap: 10px;
    font-family: "Montserrat", sans-serif;
    font-weight: 500;
    font-size: 24px;
    letter-spacing: 0.14em;
    color: var(--ink);
    text-transform: uppercase;
  }
</style>
</head>
<body>
<main class="canvas">
  <section class="card card-front" aria-label="Card front">
    <div class="front-lockup">
      <div class="brand-name-front"><span class="brand-dot"></span>VELTRIX</div>
      <h1 class="tagline">Speed that <span class="tagline-accent">earns trust</span></h1>
    </div>
  </section>

  <section class="card card-back" aria-label="Card back">
    <div class="person">
      <p class="person-name">Daniel Reyes</p>
      <p class="person-title">Co-Founder &amp; CEO</p>
    </div>
    <ul class="contact">
      <li>555.014.2290</li>
      <li>reyes@withveltrix.example</li>
      <li>www.withveltrix.example</li>
    </ul>
    <div class="wordmark"><span class="brand-dot"></span>Veltrix</div>
  </section>
</main>
</body>
</html>
```